New Business Card Design Project

I would like my card design to look exactly like the logo, design, layout, and print of the current attached file. The only change I would like made would be for the print to say THE KMR GROUP instead of THE MORALES GROUP. Basically, just replace his group name with my group name. I would also like the backgroud to be the same texture and color as the attached file. I love the dark blue lettering and house logo on the card.

I am completely open to the rest of the card design. I just want something clean and simple. Only basic contact info required on the card. Maybe just name: Wade K Holmer and cell # 555.014.2289 and email wade@thepxbroker.com

```html
<!DOCTYPE html>
<html lang="en">
<head>
<meta charset="utf-8">
<title>The KMR Group – Business Card</title>
<link href="https://fonts.googleapis.com/css2?family=Montserrat:wght@300;400;700&display=swap" rel="stylesheet">
<style>
  :root {
    --navy: #1b1745;
    --navy-deep: #120f33;
    --paper: #f3f3f1;
    --ink-grey: #6b6b72;
    --stage: #d9d9dc;
  }
  * { margin: 0; padding: 0; box-sizing: border-box; }
  html, body {
    width: 1200px; height: 900px; overflow: hidden;
    background: var(--stage);
    font-family: 'Montserrat', sans-serif;
  }
  .canvas {
    width: 1200px; height: 900px;
    display: flex; flex-direction: column;
    align-items: center; justify-content: center; gap: 60px;
  }
  .card {
    position: relative;
    width: 630px; height: 360px;
    box-shadow: 0 10px 30px rgba(0,0,0,.18);
  }
  /* back side */
  .card-back {
    background: linear-gradient(135deg, var(--navy) 0%, var(--navy-deep) 100%);
    display: flex; align-items: center; justify-content: center; gap: 18px;
  }
  .card-back .brand-mark { width: 34px; height: 34px; background: var(--paper); }
  .card-back .brand-name {
    color: var(--paper); font-weight: 300;
    font-size: 34px; letter-spacing: 8px;
  }
  /* front side */
  .card-front { background: var(--navy); }
  .card-front .panel { position: absolute; inset: 0; }
  .lockup {
    position: absolute; left: 64px; top: 150px;
    display: flex; align-items: center; gap: 20px;
  }
  .lockup .brand-mark { width: 42px; height: 42px; background: var(--navy); }
  .lockup .brand-name {
    color: var(--navy); font-weight: 300;
    font-size: 21px; letter-spacing: 5px; line-height: 1.15;
  }
  .contact {
    position: absolute; left: 370px; top: 122px;
    color: var(--navy);
  }
  .contact .person {
    font-weight: 700; font-size: 19px; letter-spacing: .5px; text-transform: uppercase;
  }
  .contact .role {
    font-weight: 400; font-size: 12px; color: var(--ink-grey);
    letter-spacing: .5px; margin: 2px 0 10px;
  }
  .contact ul { list-style: none; }
  .contact li {
    display: flex; align-items: center; gap: 9px;
    font-size: 13px; color: var(--ink-grey); line-height: 20px;
  }
  .contact svg { width: 11px; height: 11px; flex: none; fill: var(--navy); }
</style>
</head>
<body>
<main class="canvas">
  <section class="card card-back" aria-label="Card back">
    <span class="brand-mark"></span>
    <span class="brand-name">THE KMR GROUP</span>
  </section>

  <section class="card card-front" aria-label="Card front">
    <svg class="panel" viewBox="0 0 630 360" aria-hidden="true">
      <polygon fill="#f3f3f1" points="0,30 380,30 394,14 630,14 630,322 440,322 426,344 0,344"/>
    </svg>

    <div class="lockup">
      <span class="brand-mark"></span>
      <div class="brand-name">THE<br>KMR<br>GROUP</div>
    </div>

    <div class="contact">
      <div class="person">Wade K Holmer</div>
      <div class="role">CEO/FOUNDER</div>
      <ul>
        <li>
          <svg viewBox="0 0 12 12"><path d="M3 0h6a1 1 0 0 1 1 1v10a1 1 0 0 1-1 1H3a1 1 0 0 1-1-1V1a1 1 0 0 1 1-1zm0 1.5v8h6v-8z"/></svg>
          555.014.2289
        </li>
        <li>
          <svg viewBox="0 0 12 12"><path d="M0 2h12v8H0z M0 2l6 4.5L12 2" fill="none" stroke="#1b1745" stroke-width="1.4"/></svg>
          wade@thepxbroker.com
        </li>
        <li>
          <svg viewBox="0 0 12 12"><circle cx="6" cy="6" r="5.2" fill="none" stroke="#1b1745" stroke-width="1.3"/><path d="M1 6h10M6 1c-2.5 3-2.5 7 0 10M6 1c2.5 3 2.5 7 0 10" fill="none" stroke="#1b1745" stroke-width="1"/></svg>
          thepxbroker.com
        </li>
      </ul>
    </div>
  </section>
</main>
</body>
</html>
```